Music portal needs a sleek mobile app design

We need an innovative, cutting edge design for our mobile app for www.loftaroundsound.com . LOFTAROUND Music is a platform that lets independent musicians upload and share their music for free. Music lovers can discover new music too.

If you visit the website, you'll get an idea of our brand colors and theme. im attaching the logo and our new discover page layout. We use "din Next LT pro" as our brand font.

We are looking for an app optimized for iOS, but can be used on Android and windows too.

Im looking for a design that flows and navigates with user intuition and is sleek, flat style in nature and has Similar apps are tunewharf, riffpantry and beatorchard.

Here are some ideas we like, but please dont copy. Come up with something similar in 'feel'

https://www.portfoliarc.net/gallery/B-TUNE-IT-Music-application/4412983

https://sketchvault.com/shots/2290518-Music-App

The most important pages/ screens for us are:
- The discover screen
- The login and sign up screens
- The splash screen
- The track player screen
- The use profile page screen
Updates

It seems no design has come close to what I was looking for so I will be requesting a refund and withdrawing this project. Thanks for your effort

Target Market(s)

music, music app, tunewharf, loftaround music, music app design

Colors
f78f20
ffcf3e
ffffff
000000

Requirements
Must have
• a sleek easy to use navigation- please create an account on loftaroundsound.com to see how the site works.
Nice to have
• Sleek screen to screen transitions
Should not have
• no 3d designs. Flat design only

```html
<!DOCTYPE html>
<html lang="en">
<head>
<meta charset="utf-8">
<title>Welcome</title>
<link rel="stylesheet" href="https://fonts.googleapis.com/css2?family=Roboto:wght@300;400;500&display=swap">
<style>
  :root {
    --orange: #f78f20;
    --amber: #ffcf3e;
    --white: #ffffff;
    --black: #000000;
    --pill-light: #f2f2f2;
    --ink: #3a3a3a;
    --dot-idle: rgba(255, 255, 255, 0.55);
  }
  * { box-sizing: border-box; margin: 0; padding: 0; }
  html, body {
    width: 677px;
    height: 1200px;
    overflow: hidden;
    background: var(--black);
  }
  .screen {
    position: relative;
    width: 677px;
    height: 1200px;
    overflow: hidden;
    font-family: "Roboto", "Helvetica Neue", Arial, sans-serif;
    color: var(--white);
  }
  .hero-photo {
    position: absolute;
    inset: 0;
    background:
      radial-gradient(ellipse 60% 30% at 75% 12%, rgba(190, 70, 70, 0.55), transparent 70%),
      radial-gradient(ellipse 55% 35% at 50% 62%, rgba(225, 220, 212, 0.55), transparent 70%),
      linear-gradient(180deg, #6a4a48 0%, #7c6a66 30%, #8e8580 55%, #a49c95 75%, #6d6a62 100%);
  }
  .hero-shade {
    position: absolute;
    inset: 0;
    background: linear-gradient(180deg, rgba(0,0,0,0.15) 0%, rgba(0,0,0,0.25) 45%, rgba(0,0,0,0.1) 100%);
  }
  .status-bar {
    position: absolute;
    top: 0; left: 0; right: 0;
    height: 45px;
    display: flex;
    align-items: center;
    justify-content: space-between;
    padding: 0 14px;
    font-size: 26px;
    font-weight: 400;
  }
  .status-left, .status-right { display: flex; align-items: center; gap: 10px; }
  .status-time {
    position: absolute;
    left: 50%;
    transform: translateX(-50%);
    font-weight: 500;
  }
  .brand-square {
    position: absolute;
    top: 345px;
    left: 279px;
    width: 118px;
    height: 112px;
    background: var(--black);
    border: 3px solid var(--orange);
  }
  .headline {
    position: absolute;
    top: 516px;
    left: 27px;
    right: 10px;
    font-size: 50px;
    font-weight: 400;
    line-height: 1.2;
    white-space: nowrap;
  }
  .intro {
    position: absolute;
    top: 592px;
    left: 34px;
    right: 22px;
    font-size: 32px;
    font-weight: 400;
    line-height: 41px;
  }
  .pager {
    position: absolute;
    top: 1026px;
    left: 0; right: 0;
    display: flex;
    justify-content: center;
    gap: 27px;
  }
  .pager-dot {
    width: 14px;
    height: 14px;
    border-radius: 50%;
    background: var(--dot-idle);
  }
  .pager-dot.is-active { background: var(--white); }
  .actions {
    position: absolute;
    top: 1083px;
    left: 36px;
    right: 36px;
    display: flex;
    justify-content: space-between;
  }
  .btn {
    width: 280px;
    height: 82px;
    border-radius: 41px;
    display: flex;
    align-items: center;
    justify-content: center;
    font-family: inherit;
    font-size: 28px;
    font-weight: 400;
    border: none;
  }
  .btn-join { background: var(--pill-light); color: var(--ink); }
  .btn-signin { background: var(--orange); color: var(--white); }
</style>
</head>
<body>
<main class="screen">
  <div class="hero-photo" role="img" aria-label="Background photo of white headphones resting on a table with a person in a red top behind"></div>
  <div class="hero-shade"></div>

  <header class="status-bar">
    <div class="status-left">
      <svg width="62" height="14" viewBox="0 0 62 14" aria-hidden="true">
        <circle cx="6" cy="7" r="5" fill="#fff"/>
        <circle cx="18" cy="7" r="5" fill="#fff"/>
        <circle cx="30" cy="7" r="5" fill="#fff"/>
        <circle cx="42" cy="7" r="4.3" fill="none" stroke="#fff" stroke-width="1.4"/>
        <circle cx="54" cy="7" r="4.3" fill="none" stroke="#fff" stroke-width="1.4"/>
      </svg>
      <span>CARRIER</span>
      <svg width="26" height="20" viewBox="0 0 26 20" aria-hidden="true">
        <path d="M13 19 L1.5 6.5 A16 16 0 0 1 24.5 6.5 Z" fill="#fff"/>
      </svg>
    </div>
    <span class="status-time">4:21 PM</span>
    <div class="status-right">
      <svg width="14" height="24" viewBox="0 0 14 24" aria-hidden="true">
        <path d="M2 6 L12 17 L7 22 L7 2 L12 7 L2 18" fill="none" stroke="#fff" stroke-width="2"/>
      </svg>
      <span>22%</span>
      <svg width="50" height="22" viewBox="0 0 50 22" aria-hidden="true">
        <rect x="1" y="1" width="43" height="20" rx="3" fill="none" stroke="#fff" stroke-width="2"/>
        <rect x="4" y="4" width="9" height="14" fill="#fff"/>
        <rect x="45" y="7" width="4" height="8" rx="1" fill="#fff"/>
      </svg>
    </div>
  </header>

  <span class="brand-square" aria-hidden="true"></span>

  <h1 class="headline">Discover music that moves.</h1>
  <p class="intro">Inspire global audiences with your music or stream unlimted music from trending artist.</p>

  <nav class="pager" aria-label="Intro pages">
    <span class="pager-dot is-active"></span>
    <span class="pager-dot"></span>
    <span class="pager-dot"></span>
  </nav>

  <div class="actions">
    <button class="btn btn-join" type="button">Join now</button>
    <button class="btn btn-signin" type="button">Sign in</button>
  </div>
</main>
</body>
</html>
```